Business Card Design Project

New Private residential substance abuse treatment facility in Mapleton, UT. Facility located in elegant 11,000 home with stunning views of the mountains. Wish to incorporate colored logo. Business name- Cedar Brook Wellness. Facility is Tudor style with traditional furnishings, an overhead picture is attached. Lettering in a simple scroll or old english style. Must be easy to read with clear moderetly large font.
Updates

It seems the project time frame listed was not correct- it is a week.

Target Market(s)

Adults 18 and over with substance abuse issues requiring residential rehabilitation. Referral base are medical/mental health professionals, families and community agencies.

Industry/Entity Type

Residential

Colors
9bcb3b
fece3e
fbee3f

Requirements
Must have
• Clear and easy to read, professional and upscale presentation. Need logo, name, title, address, phone, fax and web page address. May add slogan later. Use same font as logo.
Nice to have
• Logo has a green mountain and a gold maple leaf so a nature themed element may work. Want to promote peaceful grounded image. Logo attached.
Should not have
• No tiny or complicated font. No modern or tech looking images. No light colored fonts.

```html
<!DOCTYPE html>
<html lang="en">
<head>
<meta charset="utf-8">
<title>Cedar Brook Wellness – Business Card</title>
<link rel="stylesheet" href="https://fonts.googleapis.com/css2?family=Fira+Sans+Condensed:wght@600;700&display=swap">
<style>
  :root {
    --backdrop: #d9d9d9;
    --card: #ffffff;
    --forest: #2f5a24;
    --gold: #c8921e;
    --ink: #3a3a3a;
  }
  * { margin: 0; padding: 0; box-sizing: border-box; }
  html, body {
    width: 1200px;
    height: 787px;
    overflow: hidden;
    background: var(--backdrop);
    font-family: "Fira Sans Condensed", "Arial Narrow", sans-serif;
  }
  .business-card {
    position: absolute;
    left: 180px;
    top: 153px;
    width: 840px;
    height: 480px;
    background: var(--card);
    overflow: hidden;
    box-shadow: 0 6px 18px rgba(0,0,0,0.18);
  }
  .brand {
    position: absolute;
    top: 52px;
    left: 0;
    width: 100%;
    display: flex;
    justify-content: center;
    align-items: center;
    gap: 14px;
  }
  .brand-dot {
    width: 22px;
    height: 22px;
    border-radius: 50%;
    background: var(--gold);
  }
  .brand-name {
    font-size: 44px;
    font-weight: 700;
    color: var(--forest);
    letter-spacing: 0.5px;
  }
  .identity {
    position: absolute;
    left: 70px;
    top: 205px;
    width: 360px;
    text-align: center;
  }
  .person-name {
    font-size: 54px;
    font-weight: 700;
    color: var(--forest);
    line-height: 1;
    letter-spacing: 1px;
  }
  .person-title {
    margin-top: 10px;
    font-size: 17px;
    font-weight: 700;
    color: var(--forest);
  }
  .divider {
    position: absolute;
    left: 470px;
    top: 192px;
    width: 3px;
    height: 112px;
    background: var(--forest);
  }
  .contact-list {
    position: absolute;
    left: 500px;
    top: 198px;
    list-style: none;
  }
  .contact-list li {
    font-size: 17px;
    font-weight: 700;
    color: var(--forest);
    line-height: 24px;
  }
  .base-bands {
    position: absolute;
    left: 0;
    bottom: 0;
    width: 840px;
    height: 480px;
  }
  .band-gold { fill: var(--gold); }
  .band-forest { fill: var(--forest); }
</style>
</head>
<body>
  <div class="business-card">
    <div class="brand">
      <span class="brand-dot"></span>
      <span class="brand-name">Cedar Brook Wellness</span>
    </div>

    <div class="identity">
      <div class="person-name">DANIEL MARSH</div>
      <div class="person-title">TITLE GOES HERE</div>
    </div>

    <div class="divider"></div>

    <ul class="contact-list">
      <li>ADRESSE:</li>
      <li>PHONE:</li>
      <li>FAX :</li>
      <li>WEBSITE:</li>
    </ul>

    <svg class="base-bands" viewBox="0 0 840 480" aria-hidden="true">
      <polygon class="band-gold" points="0,440 840,410 840,428 0,456"/>
      <polygon class="band-forest" points="0,456 840,428 840,480 0,480"/>
    </svg>
  </div>
</body>
</html>
```